Letterhead and envelope design

Using current logo and colours I would like to have a new design done for a stationary set to be printed.

The new files should include logo, web and email address as well as,mailing address and phone number

Tom Varsholt
Varsholt Construction Inc
Box 27 Site 16 RR4
Okotoks AB
T4R 2K9
Cell : 403-555-0186
Email: tom@varsholtconstruction-example.com
web: varsholtconstruction-example.com

```html
<!DOCTYPE html>
<html lang="en">
<head>
<meta charset="utf-8">
<title>Varsholt Construction Stationery</title>
<link rel="stylesheet" href="https://fonts.googleapis.com/css2?family=Lato:wght@400;700&family=Roboto:wght@400;700&family=Great+Vibes&display=swap">
<style>
  :root {
    --navy: #013565;
    --orange: #e99b00;
    --paper: #ffffff;
    --backdrop: #acaaab;
    --ink: #2b2b2b;
    --fold: #d2d2d2;
    --watermark: #f6f7f9;
  }
  * { box-sizing: border-box; margin: 0; padding: 0; }
  html, body { width: 1200px; height: 800px; overflow: hidden; }
  body { background: var(--backdrop); position: relative; font-family: "Lato", sans-serif; color: var(--ink); }

  .sheet { position: absolute; background: var(--paper); overflow: hidden; }

  .brand { position: absolute; display: flex; align-items: center; }
  .brand-dot { border-radius: 50%; background: var(--navy); flex: none; }
  .brand-name { font-family: "Roboto", sans-serif; font-weight: 700; color: var(--navy); line-height: 1.1; letter-spacing: 0.2px; }

  .wave { position: absolute; left: 0; bottom: 0; width: 100%; display: block; }

  /* Envelope front */
  .envelope-front { left: 48px; top: 142px; width: 573px; height: 257px; }
  .envelope-front .brand { left: 25px; top: 18px; gap: 13px; }
  .envelope-front .brand-dot { width: 64px; height: 64px; }
  .envelope-front .brand-name { font-size: 14px; }
  .return-address { position: absolute; left: 32px; top: 94px; font-family: "Roboto", sans-serif; font-size: 15px; line-height: 17.5px; color: #111; }
  .envelope-front .wave { height: 86px; }

  /* Envelope back */
  .envelope-back { left: 47px; top: 424px; width: 573px; height: 263px; }
  .envelope-back svg { position: absolute; left: 0; top: 0; }

  /* Letterhead */
  .letterhead { left: 642px; top: 39px; width: 512px; height: 723px; }
  .letterhead .brand { left: 29px; top: 27px; gap: 8px; }
  .letterhead .brand-dot { width: 72px; height: 72px; }
  .letterhead .brand-name { font-size: 15px; }
  .sender { position: absolute; left: 323px; top: 26px; padding-left: 9px; border-left: 1px solid var(--orange); font-family: "Roboto", sans-serif; font-size: 8.6px; line-height: 11.2px; color: #111; }
  .sender .gap { height: 4px; }
  .sender .row { display: flex; align-items: center; gap: 4px; }
  .sender svg { width: 7px; height: 7px; flex: none; }
  .watermark { position: absolute; left: 120px; top: 242px; width: 310px; height: 310px; border-radius: 50%; background: var(--watermark); }
  .letter { position: absolute; left: 38px; top: 185px; width: 443px; font-size: 9.2px; line-height: 11.3px; }
  .letter p { margin: 0; }
  .letter .date { margin-bottom: 13px; font-size: 10px; }
  .letter .recipient { margin-bottom: 13px; font-size: 9.6px; line-height: 12px; }
  .letter .salutation { font-weight: 700; font-size: 12px; margin: 4px 0 11px; }
  .letter .body { text-align: justify; margin-bottom: 11px; }
  .letter .closing { margin-top: 24px; }
  .letter .signature { font-family: "Great Vibes", cursive; font-size: 24px; line-height: 30px; margin-top: 12px; color: #111; }
  .letterhead .wave { height: 95px; }
</style>
</head>
<body>

  <section class="sheet envelope-front" aria-label="Envelope front">
    <div class="brand">
      <span class="brand-dot"></span>
      <span class="brand-name">VARSHOLT<br>CONSTRUCTION</span>
    </div>
    <address class="return-address" style="font-style:normal">
      Varsholt Construction Inc<br>
      Box 27 Site 16 RR4<br>
      Okotoks AB T4R 2K9
    </address>
    <svg class="wave" viewBox="0 0 512 95" preserveAspectRatio="none" aria-hidden="true">
      <path fill="var(--orange)" d="M0,26 C40,0 100,-2 200,18 C300,40 360,58 420,56 C470,54 495,30 512,5 L512,14 C490,40 460,60 420,62 C360,64 300,48 200,26 C110,8 40,10 0,38 Z"/>
      <path fill="var(--navy)" d="M0,45 C50,18 110,20 200,38 C300,58 360,72 420,72 C470,72 495,50 512,22 L512,95 L0,95 Z"/>
    </svg>
  </section>

  <section class="sheet envelope-back" aria-label="Envelope back">
    <svg width="573" height="263" viewBox="0 0 573 263" aria-hidden="true">
      <path fill="none" stroke="var(--fold)" stroke-width="1" d="M15,60 L7,257 L1,262 M558,60 L566,257 L572,262"/>
      <path fill="var(--navy)" d="M0,0 L573,0 L557,55 Q549,82 522,82 L51,82 Q24,82 16,55 Z"/>
      <circle cx="286" cy="41" r="33" fill="none" stroke="var(--paper)" stroke-width="1.2"/>
    </svg>
  </section>

  <section class="sheet letterhead" aria-label="Letterhead">
    <div class="watermark" aria-hidden="true"></div>
    <div class="brand">
      <span class="brand-dot"></span>
      <span class="brand-name">VARSHOLT<br>CONSTRUCTION</span>
    </div>
    <div class="sender">
      <div>Varsholt Construction Inc</div>
      <div>Box 27 Site 16 RR4</div>
      <div>Okotoks AB T4R 2K9</div>
      <div class="gap"></div>
      <div class="row"><svg viewBox="0 0 10 10"><path fill="var(--orange)" d="M2,0.5 L4,0.5 L4.8,3 L3.5,4 Q4.5,6 6,6.5 L7,5.2 L9.5,6 L9.5,8 Q9.5,9.5 8,9.5 Q1,9 0.5,2 Q0.5,0.5 2,0.5 Z"/></svg>&nbsp;403-555-0186</div>
      <div class="row"><svg viewBox="0 0 10 10"><rect x="0.5" y="2" width="9" height="6.5" fill="var(--orange)"/><path d="M0.5,2 L5,5.8 L9.5,2" fill="none" stroke="#fff" stroke-width="0.9"/></svg>Email: tom@varsholtconstruction-example.com</div>
      <div class="row"><svg viewBox="0 0 10 10"><circle cx="5" cy="5" r="4.5" fill="var(--orange)"/><path d="M0.5,5 H9.5 M5,0.5 V9.5" stroke="#fff" stroke-width="0.7"/></svg>web: varsholtconstruction-example.com</div>
    </div>

    <div class="letter">
      <p class="date">January-03-2020</p>
      <p class="recipient">Mr, Peter Lang<br>President</p>
      <p class="recipient">Northgate Corporation<br>123 Street Name, Suite# 10<br>City, State, 120023</p>
      <p class="salutation">Dear Mr, Peter</p>
      <p class="body">Lorem ipsum dolor sit amet, consectetur adipisicing elit, sed do eiusmod tempor incididunt ut labore et dolore magna aliqua. Ut enim ad minim veniam, quis nostrud exercitation ullamco laboris nisi ut aliquip ex ea commodo consequat. Duis aute irure dolor in reprehenderit in voluptate velit esse cillum dolore eu fugiat nulla pariatur.</p>
      <p class="body">Lorem ipsum dolor sit amet, consectetur adipisicing elit, sed do eiusmod tempor incididunt ut labore et dolore magna aliqua. Ut enim ad minim veniam, quis nostrud exercitation ullamco laboris nisi ut aliquip ex ea commodo consequat. Duis aute irure dolor in reprehenderit in voluptate velit esse cillum dolore eu fugiat nulla pariatur.</p>
      <p class="body">Lorem ipsum dolor sit amet, consectetur adipisicing elit, sed do eiusmod tempor incididunt ut labore et dolore magna aliqua. Ut enim ad minim veniam, quis nostrud exercitation ullamco laboris nisi ut aliquip ex ea commodo consequat.</p>
      <p class="body">Excepteur sint occaecat cupidatat non proident, sunt in culpa qui officia deserunt mollit anim id est laborum. re et dolore magnam aliquam quaerat voluptatem.</p>
      <p class="closing">Regards</p>
      <p class="signature">Daniel Hart</p>
    </div>

    <svg class="wave" viewBox="0 0 512 95" preserveAspectRatio="none" aria-hidden="true">
      <path fill="var(--orange)" d="M0,26 C40,0 100,-2 200,18 C300,40 360,58 420,56 C470,54 495,30 512,5 L512,14 C490,40 460,60 420,62 C360,64 300,48 200,26 C110,8 40,10 0,38 Z"/>
      <path fill="var(--navy)" d="M0,45 C50,18 110,20 200,38 C300,58 360,72 420,72 C470,72 495,50 512,22 L512,95 L0,95 Z"/>
    </svg>
  </section>

</body>
</html>
```